House Builder and Property Development Card Design and Logo

I need a business card design for a building and property development company.
Colour scheme of Dark Grey and Green, I would like it bold, sharp and professional.
No logo yet done, I'm open to options but please stay away from the usual- house, roof, hammers etc.
Thanks Rob

Please be aware that on the business card information section the WHRC # 5528391 is a licence number and my phone number 0492837165. The numbers are close together and could be mistaken as one whole number 

Thank you

                                   

Industry/Entity Type

Building

Contact Information for Business Card

VARGA BUILD & DEVELOPMENT.
Residential Building & Property Development
Robert Varga - Director
WHRC # 5528391
0492837165
rob@vargabuild.example.com.au

Requirements
Must have
• Bold Business name
Dark grey and green colours
Should not have
• roof outline or hammer logo

```html
<!DOCTYPE html>
<html lang="en">
<head>
<meta charset="utf-8">
<title>Varga Build &amp; Development – Business Card</title>
<link rel="stylesheet" href="https://fonts.googleapis.com/css2?family=Open+Sans:wght@400;600;700;800&display=swap">
<style>
  :root {
    --backdrop-light: #e6e0da;
    --backdrop-dark: #c4b8ad;
    --card-edge: #111111;
    --timber-light: #858585;
    --timber-mid: #6f6f6f;
    --timber-dark: #5c5c5c;
    --brand-ink: #262626;
    --brand-green: #6fbf3a;
    --text-light: #f2f2f2;
    --text-dark: #1a1a1a;
  }
  * { box-sizing: border-box; margin: 0; padding: 0; }
  html, body { width: 1200px; height: 901px; overflow: hidden; }
  body {
    background: radial-gradient(ellipse at 50% 40%, var(--backdrop-light) 0%, var(--backdrop-dark) 100%);
    font-family: "Open Sans", Arial, sans-serif;
    position: relative;
  }
  .card {
    position: absolute;
    top: 296px;
    width: 540px;
    height: 310px;
    border-radius: 26px;
    background: var(--card-edge);
    padding: 9px;
  }
  .card--front { left: 40px; }
  .card--back { left: 620px; }
  .card__surface {
    position: relative;
    width: 100%;
    height: 100%;
    border-radius: 18px;
    overflow: hidden;
  }
  .card__timber {
    position: absolute;
    inset: 0;
    background:
      linear-gradient(180deg, rgba(255,255,255,0.05) 0%, rgba(0,0,0,0.08) 100%),
      linear-gradient(90deg, var(--timber-mid) 0%, var(--timber-light) 45%, var(--timber-mid) 75%, var(--timber-dark) 100%);
  }
  .wordmark {
    position: absolute;
    color: var(--brand-ink);
    font-weight: 700;
    line-height: 1;
  }
  .wordmark__name { font-size: 64px; letter-spacing: 1px; line-height: 1.15; }
  .wordmark__sub { font-size: 15px; letter-spacing: 0.5px; margin-top: 2px; }
  .card--front .wordmark { left: 118px; top: 80px; }
  .tagline {
    position: absolute;
    left: 122px;
    top: 186px;
    color: var(--text-light);
    font-size: 15px;
    font-weight: 600;
    line-height: 1.3;
    letter-spacing: 0.5px;
    text-transform: uppercase;
  }
  .card--back .wordmark { left: 26px; top: 124px; }
  .card--back .wordmark__name { font-size: 54px; }
  .card--back .wordmark__sub { font-size: 13px; }
  .divider {
    position: absolute;
    left: 282px;
    top: 24px;
    bottom: 24px;
    width: 2px;
    background: var(--brand-green);
  }
  .contact {
    position: absolute;
    left: 302px;
    top: 48px;
    right: 14px;
    color: var(--text-light);
  }
  .contact__name { font-size: 20px; font-weight: 700; line-height: 1.2; }
  .contact__role {
    font-size: 9px;
    font-weight: 700;
    color: var(--brand-green);
    letter-spacing: 0.5px;
    margin-bottom: 26px;
  }
  .contact__line {
    display: flex;
    align-items: center;
    gap: 8px;
    font-size: 11.5px;
    line-height: 1.8;
    white-space: nowrap;
  }
  .contact__line svg { width: 11px; height: 11px; flex: none; }
  .contact__licence { font-size: 13px; margin-top: 20px; letter-spacing: 0.3px; }
</style>
</head>
<body>

  <section class="card card--front">
    <div class="card__surface">
      <div class="card__timber" role="img" aria-label="Grey weathered timber grain texture"></div>
      <div class="wordmark">
        <div class="wordmark__name">Varga</div>
        <div class="wordmark__sub">BUILD AND DEVELOPMENT</div>
      </div>
      <p class="tagline">Residential Building and<br>Property Development</p>
    </div>
  </section>

  <section class="card card--back">
    <div class="card__surface">
      <div class="card__timber" role="img" aria-label="Grey weathered timber grain texture"></div>
      <div class="wordmark">
        <div class="wordmark__name">Varga</div>
        <div class="wordmark__sub">BUILD AND DEVELOPMENT</div>
      </div>
      <div class="divider"></div>
      <div class="contact">
        <div class="contact__name">Robert Varga</div>
        <div class="contact__role">DIRECTOR</div>
        <div class="contact__line">
          <svg viewBox="0 0 12 12" aria-hidden="true"><path fill="#1a1a1a" d="M1 3.5C1 2 2.2 1.5 6 1.5S11 2 11 3.5V5H8.5V3.8H3.5V5H1zM2.5 6h7l1 4.5h-9z"/></svg>
          <span>04 92 837 165</span>
        </div>
        <div class="contact__line">
          <svg viewBox="0 0 12 12" aria-hidden="true"><rect x="1" y="2.5" width="10" height="7" fill="#1a1a1a"/><path d="M1.5 3l4.5 3.5L10.5 3" stroke="#8a8a8a" stroke-width="1" fill="none"/></svg>
          <span>rob@vargabuild.example.com.au</span>
        </div>
        <div class="contact__licence">WHRC#5528391</div>
      </div>
    </div>
  </section>

</body>
</html>
```